Bright Harbor Family Law Firm Website Renovation

We need a website redesign in SquareSpace that is more modern, user friendly, on brand, less cluttered, easier to navigate, conveys clearly what our services are, and has clear, visible calls to action.

We would like to hire and work with the winning designer to complete the remaining pages of the site.
Updates

Gathering more feedback

Target Market(s)

Couples looking for divorce representation or mediation who have a conscious, progressive mindset. They are self-aware and personal development plays an important role in their lives. They want an amicable interaction and aspire to have a healthy relationship after divorce.

Age range: 30-60
Income 100K+ household

Industry/Entity Type

Family Law

Font styles to use
Sans Serif

Colors
85acd3
33a6d7
50c0af
a0cd3a

Requirements
Must have
• Please see attached doc for full creative brief details.

"Changing the way people divorce" on top of site.
Images that show happy clients and that represent males and females. Diversity inclusion is also be important.
We are looking for warm, welcoming design and imagery.
Should not have
• Not heavily attorney focused.
Please see attached brief for full description.

```html
<!DOCTYPE html>
<html lang="en">
<head>
<meta charset="utf-8">
<title>Bright Harbor Family Law — Changing the Way People Divorce</title>
<link rel="stylesheet" href="https://fonts.googleapis.com/css2?family=Open+Sans:wght@300;400;600;700&family=Tinos:wght@400;700&display=swap">
<style>
:root{
  --teal:#3aa39c;
  --sky:#33a6d7;
  --green:#a0cd3a;
  --navy:#161c26;
  --slate:#3a4556;
  --blue-band:#2b5d88;
  --blue-deep:#274f74;
  --ink:#2b2f36;
  --muted:#6b7079;
  --soft:#f1f2f4;
  --white:#ffffff;
}
*{box-sizing:border-box;margin:0;padding:0}
html,body{width:1200px;height:4500px;overflow:hidden;background:var(--white)}
body{font-family:"Open Sans",Arial,sans-serif;color:var(--ink);position:relative}
section,header,footer{position:absolute;left:0;width:1200px}
.abs{position:absolute}
.serif{font-family:"Tinos","Times New Roman",serif}
.btn-dark{position:absolute;background:var(--slate);color:#fff;font-size:13px;letter-spacing:.5px;display:flex;align-items:center;justify-content:center;border:1px solid #27303d}
.btn-line{position:absolute;border:1px solid rgba(255,255,255,.8);color:#fff;display:flex;align-items:center;justify-content:center}
.photo{position:absolute}

/* header */
.site-header{top:0;height:80px;background:#fff}
.nav a{position:absolute;top:38px;font-size:15px;color:#4a4f57;text-decoration:none}
.nav a.active{color:var(--teal)}
.nav .active-bar{position:absolute;left:119px;top:74px;width:78px;height:4px;background:var(--teal)}
.call-badge{position:absolute;right:0;top:0;width:253px;height:30px;background:var(--teal);color:#fff;font-family:"Tinos",serif;font-weight:700;font-size:17px;display:flex;align-items:center;justify-content:center}
.brand{position:absolute;left:531px;top:0;width:145px;height:148px;background:#fff;border:1px solid #d9dcdf;border-top:none;display:flex;flex-direction:column;align-items:center;justify-content:center;z-index:5}
.brand .dot{width:46px;height:46px;border-radius:50%;background:var(--teal);margin-bottom:12px}
.brand .name{font-family:"Open Sans",sans-serif;font-size:12px;font-weight:600;color:#3b4048;text-align:center;line-height:1.35;letter-spacing:1px}

/* hero */
.hero{top:80px;height:491px}
.hero .photo{inset:0;background:linear-gradient(100deg,#4a3f38 0%,#6b5f55 40%,#5a4c45 70%,#3a302b 100%)}
.hero .shade{position:absolute;inset:0;background:rgba(20,18,18,.35)}
.hero h1{position:absolute;top:190px;width:100%;text-align:center;font-size:44px;color:#fff;font-weight:700}
.hero .sub{position:absolute;top:258px;width:100%;text-align:center;font-size:35px;color:#fff}
.hero .phone{position:absolute;top:312px;width:100%;text-align:center;font-size:35px;color:#fff}
.hero .btn-line{left:437px;top:383px;width:367px;height:56px;font-size:19px;font-family:"Open Sans",sans-serif}

/* intro band */
.intro{top:571px;height:219px;background:var(--navy)}
.intro h2{position:absolute;left:145px;top:68px;width:420px;font-size:17px;line-height:1.6;color:#fff;font-weight:700;letter-spacing:.5px}
.intro h2 .g{color:var(--green)}
.intro h2 .b{color:var(--sky)}
.intro .lead{position:absolute;left:656px;top:65px;width:400px;font-size:13.5px;font-style:italic;color:var(--sky);line-height:1.4}
.intro .body{position:absolute;left:656px;top:112px;width:400px;font-size:11px;color:#d9dde3;line-height:1.35}

/* split sections */
.split h3{position:absolute;font-family:"Tinos",serif;font-weight:700;color:var(--sky);font-size:17px;letter-spacing:1px}
.split .lead{position:absolute;font-style:italic;font-weight:300;color:#555a62;font-size:16px;line-height:1.55}
.split .body{position:absolute;font-size:12.5px;color:#6b7079;line-height:1.6}
.split .body .hl{color:var(--sky)}
.help{top:790px;height:485px}
.help .photo{left:600px;top:0;width:600px;height:485px;background:linear-gradient(135deg,#6d5a48,#8e7760 45%,#3e4a4f 60%,#5c4634)}

.questions{top:1275px;height:262px}
.questions .photo{inset:0;background:linear-gradient(90deg,#2a2623,#4a413a 50%,#2e2925)}
.questions h2{position:absolute;top:65px;width:100%;text-align:center;font-family:"Tinos",serif;font-weight:700;font-size:29px;color:#fff;letter-spacing:.5px}
.questions .btn-line{left:428px;top:157px;width:342px;height:55px;font-size:16px;letter-spacing:.5px}

.together{top:1537px;height:486px}
.together .photo{left:0;top:0;width:600px;height:486px;background:linear-gradient(160deg,#d7dadd,#b8bcc1 50%,#e3e5e7)}

/* profile */
.profile{top:2023px;height:335px;background:var(--blue-band)}
.profile .frame{position:absolute;left:145px;top:51px;width:234px;height:234px;border:6px solid #1f3f5e;background:#d8dde2}
.profile .frame .photo{inset:0;background:linear-gradient(180deg,#e4e6e8,#c9ccd0)}
.profile h3{position:absolute;left:420px;top:67px;font-family:"Tinos",serif;font-weight:700;color:var(--green);font-size:17px;letter-spacing:1px}
.profile .role{position:absolute;left:420px;top:100px;font-size:12px;font-style:italic;color:#dfe6ee}
.profile .tagline{position:absolute;left:420px;top:122px;width:620px;font-size:25px;font-weight:300;color:#fff;line-height:1.1}
.profile .body{position:absolute;left:420px;top:225px;width:620px;font-size:12.5px;color:#e5ebf1;line-height:1.55}

/* bespoke */
.bespoke{top:2358px;height:486px}
.bespoke h2{position:absolute;left:145px;top:105px;width:420px;font-size:26px;font-weight:400;color:#2b2f36;line-height:1.2}
.bespoke .kicker{position:absolute;left:145px;top:198px;font-size:13px;font-style:italic;color:#8b9097;letter-spacing:1px}
.bespoke .body{position:absolute;left:145px;top:235px;width:415px;font-size:10px;color:#8b9097;line-height:1.7}
.bespoke .video-bg{position:absolute;left:600px;top:0;width:600px;height:486px;background:#8aa8c9}
.bespoke .video{position:absolute;left:600px;top:78px;width:600px;height:335px;background:linear-gradient(180deg,#9fb6c9 0%,#c8c7b6 50%,#7e7d62 100%)}
.bespoke .controls{position:absolute;left:600px;top:378px;width:600px;height:35px;background:rgba(0,0,0,.25)}
.bespoke .controls .bar{position:absolute;left:20px;right:20px;top:2px;height:2px;background:rgba(255,255,255,.5)}

/* testimonials */
.quotes{top:2844px;height:218px;background:var(--soft)}
.quote{position:absolute;top:87px;font-size:13px;font-style:italic;color:#3b4048;line-height:1.6}
.quote .mark{position:absolute;left:-28px;top:-4px;font-family:"Tinos",serif;font-size:40px;font-weight:700;color:var(--blue-band);line-height:1}

/* services */
.services{top:3062px;height:804px}
.services h2{position:absolute;left:145px;top:103px;font-size:26px;font-weight:400;color:#2b2f36}
.tile{position:absolute;width:215px}
.tile .photo{position:relative;width:215px;height:145px}
.tile .label{text-align:center;font-size:11px;font-weight:600;color:var(--blue-band);margin-top:12px}

/* features */
.features{top:3866px;height:266px;background:var(--blue-deep)}
.feature{position:absolute;top:0;width:230px;text-align:center;color:#fff}
.feature svg{position:absolute;left:98px;top:76px}
.feature h4{position:absolute;top:130px;width:100%;font-size:12px;font-weight:600;letter-spacing:.3px}
.feature p{position:absolute;top:150px;width:100%;font-size:10.5px;line-height:1.5;color:#dbe3ec}

/* ask */
.ask{top:4132px;height:209px}
.ask h2{position:absolute;left:145px;top:56px;font-size:26px;font-weight:400;color:#2b2f36}
.ask p{position:absolute;left:145px;top:103px;width:530px;font-size:12.5px;color:#3b4048;line-height:1.55}
.ask .btn-dark{left:895px;top:75px;width:160px;height:44px;font-size:11px;font-weight:700;color:var(--green);background:var(--slate)}

/* footer */
.site-footer{top:4341px;height:159px;background:var(--soft)}
.site-footer .addr{position:absolute;left:145px;top:31px;font-size:10px;color:#4a4f57;line-height:1.4}
.site-footer .hours{position:absolute;left:380px;top:36px;font-size:10px;color:#4a4f57;line-height:2}
.site-footer .hours div{display:flex;align-items:center;gap:6px}
.social{position:absolute;left:964px;top:51px;display:flex;gap:4px}
.social span{width:14px;height:14px;background:#4f5a68;display:block}
.copy{position:absolute;left:795px;top:77px;font-size:9px;color:#8b9097}
</style>
</head>
<body>

<header class="site-header">
  <nav class="nav">
    <a class="active" style="left:146px">Home</a>
    <a style="left:212px">Our Services</a>
    <a style="left:340px">Testimonials</a>
    <a style="left:450px">about Us</a>
    <a style="left:718px">FAQs</a>
    <a style="left:827px">Resources</a>
    <a style="left:962px">Schedule/Contact</a>
    <span class="active-bar" style="left:119px"></span>
  </nav>
  <div class="brand">
    <span class="dot"></span>
    <span class="name">BRIGHT HARBOR<br>FAMILY LAW</span>
  </div>
  <div class="call-badge">Call: (555) 214-3090</div>
</header>

<section class="hero">
  <div class="photo" role="img" aria-label="Smiling diverse couple meeting with a mediator at a table"></div>
  <div class="shade"></div>
  <h1 class="serif">Changing the Way People Divorce.</h1>
  <div class="sub serif">Call to learn how we can help</div>
  <div class="phone serif">(555) 214-3090</div>
  <div class="btn-line">Schedule a free information call</div>
</section>

<section class="intro">
  <h2 class="serif">EFFICIENT AND POSITIVE FAMILY LEGAL TRANSITIONS <span class="g">WITHOUT COSTLY,</span> <span class="b">PAINFUL LEGAL BATTLES.</span></h2>
  <p class="lead">Traditionally, divorcing couples had two options: hire lawyers and go to battle, or avoid divorce professionals.</p>
  <p class="body">Many people don't want to add unnecessary financial and emotional costs to their divorce, but they need professional help to ensure they come away with a good parenting plan and fair financial outcomes.</p>
</section>

<section class="split help">
  <h3 style="left:145px;top:93px">HELP JUST FOR YOU</h3>
  <p class="lead" style="left:145px;top:147px;width:410px">If mediation is not possible, you need a lawyer to advise, negotiate, and possibly advocate for you.</p>
  <p class="body" style="left:145px;top:213px;width:410px">Our experienced Bright Harbor Family™ lawyers offer <span class="hl">clear, confident, and highly effective advice and representation</span> while attempting to minimize financial and emotional costs to you and your family.</p>
  <div class="btn-dark" style="left:145px;top:359px;width:121px;height:40px">LEARN MORE</div>
  <div class="photo" role="img" aria-label="Stack of law books with a wooden gavel"></div>
</section>

<section class="questions">
  <div class="photo" role="img" aria-label="Hand signing a document, darkened background"></div>
  <h2>GET YOUR QUESTIONS ANSWERED</h2>
  <div class="btn-line">SCHEDULE A FEE INFORMATION CALL</div>
</section>

<section class="split together">
  <div class="photo" role="img" aria-label="Overhead view of a couple meeting with mediators around a table"></div>
  <h3 style="left:657px;top:80px">WORK TOGETHER</h3>
  <p class="lead" style="left:652px;top:125px;width:405px">Mediation is possible when both spouses are willing to negotiate their divorce agreements in good faith, with the help of a neutral mediator.</p>
  <p class="body" style="left:652px;top:209px;width:405px">Bright Harbor Family™ attorney-mediators are experienced family lawyers and are skilled at helping clients <span class="hl">reach fair, workable agreements, without the cost and damage of the conventional divorce process.</span></p>
  <div class="btn-dark" style="left:653px;top:341px;width:121px;height:40px">LEARN MORE</div>
</section>

<section class="profile">
  <div class="frame"><div class="photo" role="img" aria-label="Portrait of the principal solicitor"></div></div>
  <h3>MAREN HOLT</h3>
  <div class="role">Principal Solicitor</div>
  <div class="tagline">Doctor of Law, Juris Doctor. Maren has been practicing family law since 2000 as a solicitor and barrister</div>
  <p class="body">Our simple, free questionnaire can help you determine if you and your spouse are suited for mediation, or if you may want legal representation for yourself.</p>
</section>

<section class="bespoke">
  <h2>A bespoke, personal service at affordable rates</h2>
  <div class="kicker">WE ARE PROUD TO SERVE YOUR FAMILY.</div>
  <p class="body">Bright Harbor Family Law &amp; Mediation LLC currently serves the legal needs of Colorado residents (including same-sex and other alternative families) in Boulder County, Denver County, Broomfield County, Larimer County, Adams County, Weld County, and Jefferson County.</p>
  <div class="btn-dark" style="left:145px;top:359px;width:121px;height:40px">LEARN MORE</div>
  <div class="video-bg"></div>
  <div class="video" role="img" aria-label="Video still of a parent and child looking over open grassland"></div>
  <div class="controls">
    <div class="bar"></div>
    <svg class="abs" style="left:18px;top:13px" width="40" height="12" viewBox="0 0 40 12"><rect x="0" y="1" width="3" height="10" fill="#fff"/><rect x="5" y="1" width="3" height="10" fill="#fff"/><path d="M22 4h3l4-3v10l-4-3h-3z" fill="#fff"/></svg>
    <span class="abs" style="left:70px;top:11px;font-size:9px;color:#fff">00:00 / 00:15</span>
  </div>
</section>

<section class="quotes">
  <svg class="abs" style="left:60px;top:88px" width="16" height="40" viewBox="0 0 16 40"><path d="M14 2L3 20l11 18" fill="none" stroke="#c5c9ce" stroke-width="1.5"/></svg>
  <div class="quote" style="left:172px;width:400px"><span class="mark">”</span>The most diligent, knowledgeable, enthusiastic, creative and thinking specialist in divorce and property settlement law”</div>
  <div class="quote" style="left:636px;width:420px"><span class="mark">”</span>Maren is intelligent, sharp and very effective. She resolved my matter in just a few months”</div>
  <svg class="abs" style="left:1125px;top:88px" width="16" height="40" viewBox="0 0 16 40"><path d="M2 2l11 18L2 38" fill="none" stroke="#c5c9ce" stroke-width="1.5"/></svg>
</section>

<section class="services">
  <h2>We deal with your problems so you could focus on your future</h2>
  <div class="tile" style="left:145px;top:165px"><div class="photo" role="img" aria-label="Chess pieces on a board" style="background:linear-gradient(180deg,#e9ebec,#3b3f44)"></div><div class="label">Family Court Applications</div></div>
  <div class="tile" style="left:376px;top:165px"><div class="photo" role="img" aria-label="Abstract wire sculpture" style="background:linear-gradient(180deg,#cdd6d9,#8d9da2)"></div><div class="label">Divorce and Separation</div></div>
  <div class="tile" style="left:608px;top:165px"><div class="photo" role="img" aria-label="Hands signing a contract" style="background:linear-gradient(180deg,#eef1f3,#b9c3ca)"></div><div class="label">Property Settlement</div></div>
  <div class="tile" style="left:840px;top:165px"><div class="photo" role="img" aria-label="Paper family cut-outs on grass" style="background:linear-gradient(180deg,#b7d36b,#4f8d2c)"></div><div class="label">Child Custody</div></div>

  <div class="tile" style="left:145px;top:355px"><div class="photo" role="img" aria-label="Wedding ring on banknotes and a pen" style="background:linear-gradient(180deg,#d9dccd,#8f9384)"></div><div class="label">Binding Financial Agreements</div></div>
  <div class="tile" style="left:376px;top:355px"><div class="photo" role="img" aria-label="Airport window with a departing plane" style="background:linear-gradient(180deg,#b5c3cf,#2c3237)"></div><div class="label">Relocation with Children</div></div>
  <div class="tile" style="left:608px;top:355px"><div class="photo" role="img" aria-label="Two businessmen standing together" style="background:linear-gradient(180deg,#e6e8ea,#2e333a)"></div><div class="label">Spousal Maintenance</div></div>
  <div class="tile" style="left:840px;top:355px"><div class="photo" role="img" aria-label="Teddy bear sitting alone on a road" style="background:linear-gradient(180deg,#8e9aa5,#4d5055)"></div><div class="label">International Child Abduction</div></div>

  <div class="tile" style="left:145px;top:546px"><div class="photo" role="img" aria-label="Glass globe on a blue background" style="background:linear-gradient(180deg,#c4d3e6,#34598c)"></div><div class="label">International Matters</div></div>
  <div class="tile" style="left:376px;top:546px"><div class="photo" role="img" aria-label="Child with a piggy bank" style="background:linear-gradient(180deg,#f2f0ed,#d8d1c8)"></div><div class="label">Child Support</div></div>
  <div class="tile" style="left:608px;top:546px"><div class="photo" role="img" aria-label="Open hand raised in a stop gesture" style="background:linear-gradient(180deg,#9ea3a8,#4a4f55)"></div><div class="label">Domestic Violence</div></div>
  <div class="tile" style="left:840px;top:546px"><div class="photo" role="img" aria-label="Elderly couple seen from behind" style="background:linear-gradient(180deg,#c2ccd5,#6d7680)"></div><div class="label">Legal Wills</div></div>
</section>

<section class="features">
  <div class="feature" style="left:141px">
    <svg width="34" height="34" viewBox="0 0 34 34" fill="none" stroke="#a0cd3a" stroke-width="2"><circle cx="17" cy="17" r="14"/><ellipse cx="17" cy="17" rx="6" ry="14"/><path d="M3 17h28M6 9h22M6 25h22"/></svg>
    <h4>A GLOBAL VIEW</h4>
    <p>We work with top family law firms<br>around the globe to ensure you<br>are adequately protected</p>
  </div>
  <div class="feature" style="left:371px">
    <svg width="34" height="34" viewBox="0 0 34 34" fill="#a0cd3a"><rect x="9" y="4" width="14" height="8" transform="rotate(35 16 8)"/><rect x="16" y="12" width="4" height="16" transform="rotate(-55 18 20)"/><rect x="4" y="28" width="18" height="4"/></svg>
    <h4>EXPERT LAWYERS</h4>
    <p>We are internationally recognised by<br>our peers as the leading experts<br>in family law.</p>
  </div>
  <div class="feature" style="left:601px">
    <svg width="34" height="34" viewBox="0 0 34 34" fill="#a0cd3a"><circle cx="10" cy="6" r="4"/><circle cx="24" cy="6" r="4"/><rect x="5" y="12" width="10" height="20" rx="2"/><rect x="19" y="12" width="10" height="20" rx="2"/></svg>
    <h4>CLIENT FOCUS</h4>
    <p>We are internationally recognised by<br>our peers as the leading experts<br>in family law.</p>
  </div>
  <div class="feature" style="left:831px">
    <svg width="34" height="34" viewBox="0 0 34 34" fill="none" stroke="#a0cd3a" stroke-width="2"><circle cx="17" cy="15" r="8" fill="#a0cd3a"/><path d="M13 26h8M14 30h6M17 1v3M4 15H1M33 15h-3M7 5l2 2M27 5l-2 2"/></svg>
    <h4>LOCAL KNOWLEDGE</h4>
    <p>Always on top of the latest developments<br>in family and inheritance law.<br>We never stop to excel</p>
  </div>
</section>

<section class="ask">
  <h2>Do you have questions about a legal issue?</h2>
  <p>Donec id arcu semper, lobortis ante sit amet, ullamcorper tellus. Maecenas consequat libero nec varius bibendum. Donec a luctus purus, quis tincidunt neque.</p>
  <div class="btn-dark">ASK AN EXPERT</div>
</section>

<footer class="site-footer">
  <div class="addr">Bright Harbor Family Law &amp;<br>Mediation LLC<br>1420 Harbor Avenue, Suite 4<br>Lakeview, Colorado 80000</div>
  <div class="hours">
    <div><svg width="10" height="10" viewBox="0 0 10 10"><circle cx="5" cy="5" r="4" fill="none" stroke="#2b5d88" stroke-width="1.2"/><path d="M5 2.5V5h2" stroke="#2b5d88" fill="none"/></svg>Monday – Friday: 9 am-5 pm</div>
    <div><svg width="10" height="10" viewBox="0 0 10 10"><path d="M2 1l2 0 1 2-1 1c.5 1 1 1.5 2 2l1-1 2 1v2c-4 0-7-3-7-7z" fill="#2b5d88"/></svg>(555) 214-3091</div>
    <div><svg width="10" height="10" viewBox="0 0 10 10"><rect x="1" y="2" width="8" height="6" fill="#2b5d88"/><path d="M1 2l4 3 4-3" stroke="#fff" fill="none" stroke-width=".8"/></svg>hello@brightharbor.example</div>
  </div>
  <div class="social"><span></span><span></span><span></span><span></span><span></span></div>
  <div class="copy">Copyright 2020 brightharbor.example &nbsp;| &nbsp;All Rights Reserved</div>
</footer>

</body>
</html>
```